We need a logo for our business which is a dental clinic (i.e. dentistry).
We would lilke designs using the colour blue, green and black incorporating the words Corvath Dental, possibly a smile or a tooth image can be considered for incorporation in the logo.

Industry/Entity Type

Dental

```html
<!DOCTYPE html>
<html lang="en">
<head>
<meta charset="utf-8">
<title>Corvath Dental – Business Card</title>
<link rel="stylesheet" href="https://fonts.googleapis.com/css2?family=Exo+2:ital,wght@0,400;0,600;1,600&display=swap">
<style>
  :root {
    --backdrop: #e4e6e8;
    --card: #ffffff;
    --brand-blue: #1ba4c9;
    --wave-blue: #5cc5e6;
    --wave-deep: #1e9fc8;
    --brand-green: #9bcb3b;
    --ink: #2a2d30;
    --ink-soft: #4b5055;
  }
  * { margin: 0; padding: 0; box-sizing: border-box; }
  html, body { width: 1200px; height: 771px; overflow: hidden; }
  body {
    background: var(--backdrop);
    font-family: "Exo 2", sans-serif;
    color: var(--ink);
    position: relative;
  }
  .card {
    position: absolute;
    top: 231px;
    width: 540px;
    height: 309px;
    background: var(--card);
    box-shadow: 0 8px 24px rgba(0,0,0,0.12);
    overflow: hidden;
  }
  .card--front { left: 40px; }
  .card--back { left: 620px; }

  .brand-name {
    font-weight: 600;
    color: var(--brand-blue);
    display: flex;
    align-items: center;
    gap: 12px;
    white-space: nowrap;
  }
  .brand-dot {
    width: 14px; height: 14px;
    border-radius: 50%;
    background: var(--brand-green);
    flex: none;
  }
  .card--front .brand-name {
    position: absolute;
    left: 50%; top: 50%;
    transform: translate(-50%, -50%);
    font-size: 38px;
  }
  .card--back .brand-name {
    position: absolute;
    left: 30px; top: 34px;
    font-size: 26px;
  }
  .address {
    position: absolute;
    left: 30px; top: 84px;
    font-size: 12px;
    line-height: 1.45;
    color: var(--ink-soft);
    font-style: italic;
  }
  .holder {
    position: absolute;
    right: 30px; top: 34px;
    text-align: right;
  }
  .holder-name { font-size: 20px; font-weight: 400; letter-spacing: 0.5px; }
  .holder-role { font-size: 12px; color: var(--ink-soft); margin-top: 2px; }
  .contact-list {
    position: absolute;
    right: 30px; top: 112px;
    list-style: none;
    text-align: right;
    font-size: 11px;
    color: var(--ink-soft);
  }
  .contact-list li {
    display: flex;
    justify-content: flex-end;
    align-items: center;
    gap: 7px;
    height: 17px;
  }
  .contact-list svg { width: 11px; height: 11px; fill: var(--ink); flex: none; }
  .wave { position: absolute; left: 0; top: 0; width: 540px; height: 309px; }
</style>
</head>
<body>
  <section class="card card--front" aria-label="Card front">
    <div class="brand-name"><span class="brand-dot"></span>Corvath Dental</div>
  </section>

  <section class="card card--back" aria-label="Card back">
    <svg class="wave" viewBox="0 0 540 309" aria-hidden="true">
      <defs>
        <linearGradient id="waveFill" x1="0" y1="0" x2="1" y2="1">
          <stop offset="0" stop-color="var(--wave-deep)"/>
          <stop offset="0.5" stop-color="var(--wave-blue)"/>
          <stop offset="1" stop-color="var(--wave-deep)"/>
        </linearGradient>
      </defs>
      <path d="M0 138 C90 150 160 200 250 226 C330 250 400 262 470 309 L0 309 Z" fill="url(#waveFill)"/>
      <path d="M0 124 C70 128 130 170 220 206 C300 236 390 250 440 282" fill="none" stroke="var(--brand-green)" stroke-width="6"/>
      <path d="M0 300 C120 290 260 250 360 262 C420 270 470 290 500 309" fill="none" stroke="var(--brand-green)" stroke-width="5"/>
    </svg>

    <div class="brand-name"><span class="brand-dot"></span>Corvath Dental</div>
    <p class="address">214 Harlow Court, Fenwick Lane<br>HBR</p>

    <div class="holder">
      <p class="holder-name">Tomas Elbury</p>
      <p class="holder-role">Managing Director</p>
    </div>

    <ul class="contact-list">
      <li>020 555 0147
        <svg viewBox="0 0 24 24"><path d="M6.6 10.8a15 15 0 0 0 6.6 6.6l2.2-2.2c.3-.3.7-.4 1-.2 1.1.4 2.3.6 3.6.6.6 0 1 .4 1 1V20c0 .6-.4 1-1 1A17 17 0 0 1 3 4c0-.6.4-1 1-1h3.5c.6 0 1 .4 1 1 0 1.3.2 2.5.6 3.6.1.3 0 .7-.2 1z"/></svg>
      </li>
      <li>020 555 0148
        <svg viewBox="0 0 24 24"><path d="M7 1h10a2 2 0 0 1 2 2v18a2 2 0 0 1-2 2H7a2 2 0 0 1-2-2V3a2 2 0 0 1 2-2zm0 3v14h10V4zm5 15.5a1 1 0 1 0 0 2 1 1 0 0 0 0-2z"/></svg>
      </li>
      <li>020 555 0149
        <svg viewBox="0 0 24 24"><path d="M6 2h12v5H6zM4 8h16a2 2 0 0 1 2 2v7h-4v5H6v-5H2v-7a2 2 0 0 1 2-2zm4 8v4h8v-4z"/></svg>
      </li>
      <li>hello@corvathdental.com
        <svg viewBox="0 0 24 24"><path d="M2 5h20v14H2zm2 2v.5l8 5 8-5V7zm0 3v7h16v-7l-8 5z"/></svg>
      </li>
      <li>www.corvathdental.com
        <svg viewBox="0 0 24 24"><path d="M12 2a10 10 0 1 0 0 20 10 10 0 0 0 0-20zm6.9 6h-3a15 15 0 0 0-1.3-3.9A8 8 0 0 1 18.9 8zM12 4c.8 1.2 1.5 2.5 1.9 4h-3.8c.4-1.5 1.1-2.8 1.9-4zM4.3 14a8 8 0 0 1 0-4h3.4a16 16 0 0 0 0 4zm.8 2h3a15 15 0 0 0 1.3 3.9A8 8 0 0 1 5.1 16zm3-8h-3a8 8 0 0 1 4.3-3.9C8.8 5.3 8.4 6.6 8.1 8zM12 20c-.8-1.2-1.5-2.5-1.9-4h3.8c-.4 1.5-1.1 2.8-1.9 4zm2.3-6H9.7a14 14 0 0 1 0-4h4.6a14 14 0 0 1 0 4zm.3 5.9c.6-1.2 1-2.5 1.3-3.9h3a8 8 0 0 1-4.3 3.9zm1.7-5.9a16 16 0 0 0 0-4h3.4a8 8 0 0 1 0 4z"/></svg>
      </li>
    </ul>
  </section>
</body>
</html>
```